HearthBay business card and stationary design

We are looking for a simple yet elegant design for our mortgage company business card and stationary.

The card should include:
Name (Doug Warley)
Title (CEO)
Phone Number (614-382-9047)
Address (48 Birchwood Terrace, Suite 315, Marlow, NJ 08214)
Email (email@hearthbay.example)
"NMLS" i.e. (NMLS 61947)
"Company NMLS" (Company NMLS 492716)

Contact Information for Business Card

See above

```html
<!DOCTYPE html>
<html lang="en">
<head>
<meta charset="utf-8">
<title>HearthBay Business Card</title>
<link href="https://fonts.googleapis.com/css2?family=Montserrat:wght@400;500;600&display=swap" rel="stylesheet">
<style>
  :root {
    --backdrop: #b1b1ad;
    --paper: #ffffff;
    --brand-blue: #27aae1;
    --navy: #1a2633;
    --ink: #1c2a38;
    --text-grey: #4a4f55;
    --emboss-grey: #a7aaae;
  }
  * { margin: 0; padding: 0; box-sizing: border-box; }
  html, body {
    width: 1200px; height: 801px; overflow: hidden;
    background: var(--backdrop);
    font-family: "Montserrat", sans-serif;
  }
  .stage {
    position: relative; width: 1200px; height: 801px;
  }
  .card {
    position: absolute; top: 252px;
    width: 520px; height: 297px;
    box-shadow: 0 14px 30px rgba(0,0,0,0.22);
    overflow: hidden;
  }
  .card-front { left: 50px; background: var(--paper); border-bottom: 3px solid var(--brand-blue); }
  .card-back { left: 630px; background: var(--navy); border-bottom: 3px solid var(--brand-blue); }

  .brand-name {
    position: absolute; left: 28px; top: 124px;
    width: 226px;
    font-size: 39px; font-weight: 500; color: var(--ink);
    letter-spacing: -0.5px; white-space: nowrap;
  }
  .divider {
    position: absolute; left: 274px; top: 78px;
    width: 1px; height: 118px; background: var(--brand-blue);
  }
  .contact {
    position: absolute; left: 292px; top: 74px;
    color: var(--text-grey); font-size: 12.5px; line-height: 1.45;
  }
  .contact-name {
    font-size: 22px; font-weight: 600; color: var(--brand-blue);
    text-transform: uppercase; letter-spacing: 0.5px; line-height: 1.1;
    white-space: nowrap;
  }
  .contact-title { font-size: 13px; margin-bottom: 8px; }
  .contact-line { display: flex; align-items: center; gap: 5px; white-space: nowrap; }
  .contact-line svg { width: 10px; height: 10px; flex: none; }

  .license-band {
    position: absolute; left: 0; right: 0; top: 246px; height: 28px;
    background: var(--brand-blue);
  }
  .license-ribbon {
    position: absolute; left: 50%; top: 240px; transform: translateX(-50%);
    height: 40px; padding: 0 30px;
    background: var(--navy);
    clip-path: polygon(14px 0, calc(100% - 14px) 0, 100% 50%, calc(100% - 14px) 100%, 14px 100%, 0 50%);
    display: flex; align-items: center;
    color: #fff; font-size: 13px; letter-spacing: 0.6px; white-space: nowrap;
  }
  .license-ribbon .sep { color: var(--brand-blue); margin: 0 6px; }

  .back-brand {
    position: absolute; left: 0; right: 0; top: 108px; text-align: center;
    font-size: 70px; font-weight: 500; color: var(--emboss-grey);
    letter-spacing: -1px; white-space: nowrap;
  }
</style>
</head>
<body>
<div class="stage">
  <section class="card card-front">
    <div class="brand-name">HearthBay</div>
    <div class="divider"></div>
    <div class="contact">
      <div class="contact-name">Doug Warley</div>
      <div class="contact-title">CEO</div>
      <div>48 Birchwood Terrace,</div>
      <div>Suite 315, Marlow, NJ 08214</div>
      <div class="contact-line">
        <svg viewBox="0 0 10 10" aria-hidden="true"><path d="M2 0.5 L3.6 2.6 L2.7 3.6 Q4 6.2 6.4 7.3 L7.4 6.4 L9.5 8 L8.3 9.5 Q2.5 8.5 0.5 1.7 Z" fill="#27aae1"/></svg>
        <span>614-382-9047</span>
      </div>
      <div class="contact-line">
        <svg viewBox="0 0 10 10" aria-hidden="true"><rect x="0.6" y="2" width="8.8" height="6" fill="none" stroke="#27aae1" stroke-width="1"/><path d="M0.6 2 L5 5.4 L9.4 2" fill="none" stroke="#27aae1" stroke-width="1"/></svg>
        <span>email@hearthbay.example</span>
      </div>
    </div>
    <div class="license-band"></div>
    <div class="license-ribbon">NMLS 61947<span class="sep">|</span>Company NMLS 492716</div>
  </section>

  <section class="card card-back">
    <div class="back-brand">HearthBay</div>
  </section>
</div>
</body>
</html>
```